Labor Day Sale Website Banner For High End Jewelry Website

We need a banner for our website (brindlyx.com) for a Labor Day Sale. The banner should be a size 1187 × 400. I have included a few pieces of jewelry to be included in the banner (do not need to use all, can use just some). The banner should say:
"Labor Day Sale"
"Save 15% on Everything!"
Use Promo Code: HALCYON

Target Market(s)

Affluent Female Consumers

Industry/Entity Type

Jewelry

Colors

Designer to choose colors to be used in the design.

```html
<!DOCTYPE html>
<html lang="en">
<head>
<meta charset="UTF-8">
<title>Labor Day Sale – brindlyx.com</title>
<link href="https://fonts.googleapis.com/css2?family=Arimo:wght@400&family=Josefin+Sans:wght@600&display=swap" rel="stylesheet">
<style>
  :root {
    --bg-light: #d4d4d4;
    --bg-mid: #7a7a7a;
    --bg-dark: #000000;
    --ribbon-red: #e0141b;
    --ribbon-deep: #8d0a0e;
    --gold-text: #f2d95c;
    --white: #ffffff;
    --gold: #c99a2e;
    --gold-light: #f0cf6a;
  }
  html, body {
    margin: 0;
    padding: 0;
    overflow: hidden;
    background: #ffffff;
  }
  .banner {
    position: relative;
    width: 1200px;
    height: 404px;
    overflow: hidden;
    background: linear-gradient(90deg, var(--bg-light) 0%, #bcbcbc 20%, var(--bg-mid) 50%, #2a2a2a 72%, var(--bg-dark) 85%);
    font-family: "Arimo", Arial, sans-serif;
    color: var(--white);
  }
  .model-photo {
    position: absolute;
    left: 0;
    top: 0;
    width: 200px;
    height: 404px;
    background: linear-gradient(180deg, #3a2418 0%, #c58a5e 22%, #c8962f 45%, #b5122f 70%, #8c0f25 100%);
  }
  .ribbon {
    position: absolute;
    left: 333px;
    top: 20px;
    width: 425px;
    height: 115px;
  }
  .ribbon-title {
    position: absolute;
    left: 345px;
    top: 46px;
    width: 400px;
    text-align: center;
    font-family: "Josefin Sans", Arial, sans-serif;
    font-weight: 600;
    font-size: 37px;
    letter-spacing: 2px;
    color: var(--white);
  }
  .rule-row {
    position: absolute;
    left: 258px;
    width: 568px;
    display: flex;
    align-items: center;
    gap: 14px;
  }
  .rule-row .rule {
    flex: 1;
    height: 3px;
    background: linear-gradient(90deg, rgba(255,255,255,0.6), var(--white));
  }
  .rule-row .rule.right {
    background: linear-gradient(90deg, var(--white), rgba(255,255,255,0.85));
  }
  .rule-row .rule-label {
    font-size: 30px;
    letter-spacing: 3px;
    white-space: nowrap;
  }
  .rule-save { top: 120px; }
  .rule-save .rule.left { flex: 0 0 212px; }
  .rule-everything { top: 252px; }
  .rule-everything .rule.left { flex: 0 0 128px; }
  .discount {
    position: absolute;
    left: 258px;
    top: 150px;
    width: 568px;
    text-align: center;
    font-size: 112px;
    line-height: 1;
    letter-spacing: 14px;
    color: var(--gold-text);
  }
  .promo {
    position: absolute;
    left: 284px;
    top: 340px;
    font-size: 31px;
    letter-spacing: 4px;
    white-space: nowrap;
  }
  .jewel {
    position: absolute;
  }
  .jewel-amethyst-studs {
    left: 905px; top: 56px; width: 92px; height: 66px;
    border-radius: 14px;
    background: radial-gradient(circle at 40% 45%, #7d3fa3 0%, #3d1a5a 55%, var(--gold) 80%);
  }
  .jewel-flower-studs {
    left: 1018px; top: 52px; width: 130px; height: 56px;
    border-radius: 28px;
    background: linear-gradient(90deg, #3b3fa8 0%, #7c4fae 45%, #c2508f 75%, #7a63c9 100%);
  }
  .jewel-pendant {
    left: 865px; top: 140px; width: 102px; height: 252px;
    border-radius: 50px 50px 50px 50px / 30px 30px 110px 110px;
    background: radial-gradient(ellipse at 50% 55%, #e9e4d2 0%, var(--gold-light) 35%, var(--gold) 70%, #6b4d12 100%);
  }
  .jewel-gold-hoops {
    left: 1000px; top: 168px; width: 143px; height: 68px;
    border-radius: 18px;
    background: linear-gradient(135deg, var(--gold-light) 0%, #d6a93a 50%, #9a7117 100%);
  }
  .jewel-bracelet {
    left: 972px; top: 252px; width: 205px; height: 138px;
    border-radius: 40px 60px 30px 60px;
    background: linear-gradient(160deg, #e2c26a 0%, #d8d6cf 35%, var(--gold) 60%, #c9c6bd 80%, #8e6b1b 100%);
  }
</style>
</head>
<body>
  <div class="banner">
    <div class="model-photo" role="img" aria-label="Photo of a bride in a red silk sari wearing layered gold necklaces and jewellery"></div>

    <svg class="ribbon" viewBox="0 0 425 115" aria-hidden="true">
      <defs>
        <linearGradient id="ribbonFace" x1="0" y1="0" x2="1" y2="0">
          <stop offset="0" stop-color="#b80d13"/>
          <stop offset="0.5" stop-color="#f01a20"/>
          <stop offset="1" stop-color="#b80d13"/>
        </linearGradient>
      </defs>
      <path d="M0 72 L55 68 L55 112 L0 112 L18 92 Z" fill="#a80c12"/>
      <path d="M425 72 L370 68 L370 112 L425 112 L407 92 Z" fill="#a80c12"/>
      <path d="M30 75 L55 112 L55 80 Z" fill="var(--ribbon-deep)"/>
      <path d="M395 75 L370 112 L370 80 Z" fill="var(--ribbon-deep)"/>
      <path d="M15 12 Q212 -10 410 12 L400 88 Q212 66 25 88 Z" fill="url(#ribbonFace)"/>
    </svg>
    <div class="ribbon-title">LABOR DAY SALE</div>

    <div class="rule-row rule-save">
      <span class="rule left"></span>
      <span class="rule-label">Save</span>
      <span class="rule right"></span>
    </div>

    <div class="discount">15%</div>

    <div class="rule-row rule-everything">
      <span class="rule left"></span>
      <span class="rule-label">on Everything!</span>
      <span class="rule right"></span>
    </div>

    <div class="promo">Use Promo Code: HALCYON</div>

    <div class="jewel jewel-amethyst-studs" role="img" aria-label="Pair of cushion-cut amethyst stud earrings in gold settings"></div>
    <div class="jewel jewel-flower-studs" role="img" aria-label="Pair of sapphire flower cluster earrings"></div>
    <div class="jewel jewel-pendant" role="img" aria-label="Gold egg-shaped pendant set with rock crystal and diamonds"></div>
    <div class="jewel jewel-gold-hoops" role="img" aria-label="Pair of hammered gold square clip earrings"></div>
    <div class="jewel jewel-bracelet" role="img" aria-label="Gold and diamond link bracelet"></div>
  </div>
</body>
</html>
```